Business Card Design Project

We consult with hotels on setting rates and maximizing a revenue strategy

Industry/Entity Type

Business

Contact Information for Business Card

I am not sure what I want. Our company offers high level consulting to hotels around the country but we are also laid back. I would like something that is professional but also shows the laid back side

```html
<!DOCTYPE html>
<html lang="en">
<head>
<meta charset="utf-8">
<title>Harborline Business Card</title>
<link rel="stylesheet" href="https://fonts.googleapis.com/css2?family=Source+Sans+3:wght@400;600&display=swap">
<style>
  :root {
    --workspace: #5d5d5d;
    --card: #ffffff;
    --guide: #5ef0ee;
    --teal: #6a9e9b;
    --teal-deep: #2e8a82;
    --teal-light: #7fb8b2;
    --brown: #2f2019;
  }
  html, body {
    margin: 0;
    padding: 0;
    overflow: hidden;
  }
  body {
    width: 1069px;
    height: 1200px;
    background: var(--workspace);
    position: relative;
    font-family: "Source Sans 3", "Myriad Pro", sans-serif;
  }
  .card {
    position: absolute;
    left: 104px;
    width: 882px;
    height: 529px;
    background: var(--card);
    box-shadow: 0 0 0 1px var(--guide);
    overflow: hidden;
  }
  .card--front { top: 32px; }
  .card--back { top: 626px; }
  .guide {
    position: absolute;
    border: 1.5px solid var(--guide);
    pointer-events: none;
    z-index: 5;
  }
  .guide--trim { left: 30px; top: 29px; width: 821px; height: 469px; }
  .guide--safe { left: 59px; top: 58px; width: 762px; height: 410px; }
  .card--back .guide--trim { left: 43px; top: 29px; width: 820px; height: 470px; }
  .card--back .guide--safe { left: 72px; top: 59px; width: 761px; height: 410px; }

  .bridge-art {
    position: absolute;
    background: linear-gradient(180deg, var(--teal-deep) 0%, var(--teal-light) 100%);
  }
  .card--front .bridge-art { left: 184px; top: 83px; width: 156px; height: 356px; }
  .card--back .bridge-art { left: 108px; top: 82px; width: 150px; height: 330px; }

  .brand {
    position: absolute;
    left: 347px;
    top: 329px;
  }
  .brand__name {
    color: var(--brown);
    font-weight: 600;
    font-size: 68px;
    letter-spacing: 1px;
    line-height: 1;
  }
  .brand__tagline {
    position: absolute;
    left: 364px;
    top: 404px;
    color: var(--brown);
    font-weight: 600;
    font-size: 25px;
    line-height: 1;
    white-space: nowrap;
  }

  .line {
    position: absolute;
    white-space: nowrap;
    transform: translateX(-50%);
    line-height: 1;
    z-index: 2;
  }
  .contact__name { left: 500px; top: 117px; font-size: 80px; font-weight: 600; color: var(--teal); letter-spacing: 0.5px; }
  .contact__title { left: 490px; top: 190px; font-size: 40px; color: var(--brown); }
  .contact__office { left: 498px; top: 256px; font-size: 36px; color: var(--teal); }
  .contact__fax { left: 498px; top: 300px; font-size: 36px; color: var(--teal); }
  .contact__email { left: 498px; top: 343px; font-size: 36px; color: var(--teal); }

  .footer-band {
    position: absolute;
    left: 40px;
    top: 406px;
    z-index: 1;
  }
  .contact__web { left: 472px; top: 414px; font-size: 44px; color: var(--teal); }
</style>
</head>
<body>
  <section class="card card--front">
    <div class="guide guide--trim"></div>
    <div class="guide guide--safe"></div>
    <div class="bridge-art" role="img" aria-label="Illustration of a gothic suspension bridge tower"></div>
    <div class="brand"><span class="brand__name">HARBORLINE</span></div>
    <div class="brand__tagline">Revenue Management Solutions</div>
  </section>

  <section class="card card--back">
    <div class="guide guide--trim"></div>
    <div class="guide guide--safe"></div>
    <svg class="footer-band" width="819" height="76" viewBox="0 0 819 76" aria-hidden="true">
      <path d="M0 76 C35 35 85 2 140 0 L819 0 L819 76 Z" fill="var(--brown)"/>
    </svg>
    <div class="bridge-art" role="img" aria-label="Illustration of a gothic suspension bridge tower"></div>
    <div class="line contact__name">DANA WELLS</div>
    <div class="line contact__title">Regional Revenue Manger</div>
    <div class="line contact__office">Office: 555-310-4821</div>
    <div class="line contact__fax">Fax: 555-310-4890</div>
    <div class="line contact__email">Dana@HarborlineRMS.com</div>
    <div class="line contact__web">www.HarborlineRMS.com</div>
  </section>
</body>
</html>
```